MORVANT EHS & S Resources

We would like BriefHarbor to update and make our environmental, health and safety resources business website more professional and using our new logo and color scheme.
https://morvantehsresources-example.com/

```html
<!DOCTYPE html>
<html lang="en">
<head>
<meta charset="utf-8">
<title>MORVANT EHS &amp; S Resources</title>
<link rel="stylesheet" href="https://fonts.googleapis.com/css2?family=Montserrat:wght@400;500;600;700&family=Oswald:wght@600&display=swap">
<style>
:root{
  --red:#e1251b;
  --blue:#00a3e8;
  --lime:#d2dc1c;
  --ink:#111111;
  --text:#222222;
  --soft:#f1f3f7;
  --white:#ffffff;
  --line:#e4e7ec;
}
*{margin:0;padding:0;box-sizing:border-box}
html,body{width:1200px;height:3578px;overflow:hidden}
body{position:relative;background:var(--white);font-family:"Montserrat",sans-serif;color:var(--text)}
.abs{position:absolute}
.btn{position:absolute;display:inline-flex;align-items:center;gap:10px;background:var(--red);color:var(--white);font-size:11.5px;font-weight:600;letter-spacing:.3px;height:37px;padding:0 20px;text-transform:uppercase}
.btn::after{content:"";width:9px;height:9px;background:var(--white)}

/* hero */
.hero-photo{position:absolute;left:0;top:0;width:1200px;height:790px;background:linear-gradient(90deg,#0f1522 0%,#283241 38%,#5e6a78 62%,#9aa5b0 82%,#c0c7cd 100%)}
.hero-cut{position:absolute;left:0;top:600px}
.topbar-phone{position:absolute;left:820px;top:14px;color:var(--white);font-size:11px;display:flex;align-items:center;gap:6px}
.social{position:absolute;width:24px;height:24px;border-radius:50%;border:1.5px solid var(--white)}
.social.on{background:var(--lime);border-color:var(--lime)}
.logo-panel{position:absolute;left:0;top:0}
.brand{position:absolute;display:flex;align-items:center;gap:10px;font-weight:700;color:var(--ink)}
.brand .mark{width:26px;height:26px;background:var(--red)}
.nav{position:absolute;top:80px;font-size:11.5px;font-weight:600;color:var(--ink);text-transform:uppercase}
.hero-kicker{position:absolute;left:150px;top:298px;color:var(--white);font-size:14.5px;font-weight:500;letter-spacing:.3px}
.hero-title{position:absolute;left:150px;top:326px;color:var(--white);font-family:"Oswald",sans-serif;font-size:44px;line-height:55px;font-weight:600;letter-spacing:.5px}

/* about */
.about-kicker{position:absolute;left:655px;top:847px;color:var(--blue);font-size:19px;font-weight:500}
.about-name{position:absolute;left:655px;top:870px;font-size:35px;font-weight:700;color:var(--ink)}
.about-name span{font-size:17px;font-weight:500}
.about-lead{position:absolute;left:655px;top:920px;width:395px;font-size:13px;line-height:21px;text-align:justify}
.about-body{position:absolute;left:655px;top:991px;width:395px;font-size:10.5px;line-height:20.8px;text-align:justify}

/* services */
.services{position:absolute;left:0;top:1257px;width:1200px;height:800px;background:var(--soft)}
.section-title{position:absolute;left:0;width:1200px;text-align:center;font-size:28px;font-weight:700;color:var(--ink)}
.card{position:absolute;width:287px;height:291px;border:1px solid var(--line);background:var(--soft);text-align:center;padding-top:32px}
.card.active{background:var(--white);border-color:var(--white);box-shadow:0 14px 30px rgba(0,0,0,.09)}
.card svg{display:block;margin:0 auto}
.card h3{font-size:15px;font-weight:600;color:var(--ink);margin-top:14px;text-transform:uppercase}
.card p{font-size:10.4px;line-height:20.8px;margin:10px 20px 0;color:var(--text)}
.card .more{display:block;margin-top:14px;font-size:11.5px;font-weight:600;color:var(--red);text-transform:uppercase}

/* commitment */
.commit-photo{position:absolute;left:0;top:2030px}
.commit-title{position:absolute;left:150px;top:2262px;color:var(--white);font-size:31.5px;line-height:44px;font-weight:700}

/* testimonials */
.person{position:absolute;left:205px;display:flex;align-items:center;gap:30px;font-size:12.5px;font-weight:600;color:var(--ink);text-transform:uppercase}
.avatar{width:55px;height:55px;border-radius:50%;background:linear-gradient(135deg,#b7a99a,#6d5c4e)}
.person-card{position:absolute;left:185px;top:2924px;width:285px;height:76px;background:var(--white);box-shadow:0 10px 26px rgba(0,0,0,.08)}
.divider{position:absolute;left:502px;top:2824px;width:3px;height:273px;background:#e1e1e1}
.divider i{position:absolute;left:0;top:28px;width:3px;height:85px;background:var(--lime)}
.stars{position:absolute;left:552px;top:2822px;color:var(--lime);font-size:22px;letter-spacing:3px}
.quote-title{position:absolute;left:554px;top:2866px;font-size:13.5px;font-weight:600;color:var(--ink)}
.quote-body{position:absolute;left:554px;top:2908px;width:468px;font-size:11.5px;line-height:22.4px}

/* footer */
.footer-bg{position:absolute;left:0;top:3100px}
.foot-brand{position:absolute;left:150px;top:3356px;width:140px;text-align:center;color:var(--white);font-size:36px;font-weight:700}
.foot-sub{position:absolute;left:150px;top:3402px;width:140px;text-align:center;color:var(--white);font-size:10.5px;font-weight:500;letter-spacing:2px}
.foot-social{position:absolute;width:24px;height:24px;border-radius:50%;border:1.5px solid var(--white)}
.foot-social.on{background:var(--lime);border-color:var(--lime)}
.foot-col{position:absolute;top:3308px;color:var(--white)}
.foot-col h4{font-size:12px;font-weight:600;letter-spacing:.5px;margin-bottom:12px;text-transform:uppercase}
.foot-col li{list-style:none;font-size:10.5px;line-height:25px}
.contact-item{display:flex;gap:9px;margin-bottom:14px;font-size:10.5px;line-height:15px}
.contact-item b{display:block;font-size:11px;font-weight:500;text-transform:uppercase}
.foot-rule{position:absolute;left:150px;top:3529px;width:900px;height:1px;background:#2c2c2c}
.copyright{position:absolute;left:0;top:3546px;width:1200px;text-align:center;color:var(--white);font-size:10.5px}
</style>
</head>
<body>

<!-- HERO -->
<div class="hero-photo" role="img" aria-label="Photo of a surveyor in a hard hat and high-visibility vest using a tablet beside a survey level on a construction site"></div>
<svg class="hero-cut" width="1200" height="190" viewBox="0 600 1200 190">
  <polygon points="0,618 600,765 1200,618 1200,632 600,783 0,632" fill="#00a3e8"/>
  <polygon points="0,632 600,783 1200,632 1200,790 0,790" fill="#ffffff"/>
</svg>

<div class="topbar-phone">
  <svg width="13" height="13" viewBox="0 0 24 24"><path fill="#fff" d="M6.6 10.8a15 15 0 0 0 6.6 6.6l2.2-2.2c.3-.3.7-.4 1-.2 1.1.4 2.3.6 3.6.6.6 0 1 .4 1 1V20c0 .6-.4 1-1 1A17 17 0 0 1 3 4c0-.6.4-1 1-1h3.5c.6 0 1 .4 1 1 0 1.2.2 2.4.6 3.6.1.3 0 .7-.2 1z"/></svg>
  555.014.2290
</div>
<span class="social" style="left:923px;top:10px"></span>
<span class="social on" style="left:957px;top:10px"></span>
<span class="social" style="left:991px;top:10px"></span>
<span class="social" style="left:1024px;top:10px"></span>

<svg class="logo-panel" width="1200" height="140">
  <polygon points="372,46 1200,46 1200,129 343,129" fill="#ffffff"/>
  <polygon points="0,35 398,35 357,139 0,139" fill="#ffffff"/>
</svg>
<div class="brand" style="left:150px;top:68px;font-size:30px"><span class="mark"></span>MORVANT</div>

<div class="nav" style="left:525px">Home</div>
<div class="nav" style="left:603px">About Us</div>
<div class="nav" style="left:705px">Services</div>
<div class="nav" style="left:803px">Security</div>
<div class="btn" style="left:902px;top:69px">Contact Us</div>

<div class="hero-kicker">WE LEAD IN EHS &amp; SECURITY RESOURCES</div>
<div class="hero-title">EXPERIENCE. REPUTATION.<br>RESPECT. RESULTS</div>
<div class="btn" style="left:150px;top:457px">Contact Us</div>

<!-- ABOUT -->
<svg class="abs" style="left:0;top:820px" width="620" height="370" viewBox="0 820 620 370">
  <polygon points="0,844 63,879 0,914" fill="#d2dc1c"/>
  <defs>
    <linearGradient id="teamTone" x1="0" y1="0" x2="1" y2="1">
      <stop offset="0" stop-color="#8a8f94"/><stop offset=".5" stop-color="#5a534c"/><stop offset="1" stop-color="#c8b9a4"/>
    </linearGradient>
    <linearGradient id="officeTone" x1="0" y1="0" x2="1" y2="1">
      <stop offset="0" stop-color="#6b5446"/><stop offset="1" stop-color="#2e2824"/>
    </linearGradient>
  </defs>
  <polygon points="353,826 556,1180 150,1180" fill="url(#teamTone)" role="img" aria-label="Photo of two engineers reviewing plans at a desk with a laptop"/>
  <polygon points="400,879 603,879 500,1062" fill="url(#officeTone)" role="img" aria-label="Photo of colleagues working at laptops in an office"/>
  <polygon points="113,1065 204,1065 150,1142" fill="#00a3e8"/>
</svg>

<div class="about-kicker">ABOUT</div>
<div class="about-name">MORVANT <span>ENS&amp;S RESOURCES</span></div>
<p class="about-lead">MORVANT EHS &amp; Security Resources Is A Woman-Owned Business Providing EHS Program Development, Training, Consulting And Skilled Professional Staffing.</p>
<p class="about-body">MORVANT Was Established To Provide Clients In All Industries With Safety, Health, Environmental, And Security Resources That Have The Experience Necessary To Meet Unique Client Requirements. We Utilize Our Extensive Network Of Professional Contacts And Robust Vetting Process To Bring Forward Top Talent To Carry Out Our Client's Objectives.</p>
<div class="btn" style="left:655px;top:1121px">Contact Us</div>

<!-- SERVICES -->
<div class="services"></div>
<h2 class="section-title" style="top:1321px">OUR SERVICES</h2>

<div class="card" style="left:150px;top:1383px">
  <svg width="72" height="68" viewBox="0 0 72 68" fill="none" stroke="#00a3e8" stroke-width="3">
    <rect x="4" y="46" width="10" height="20"/><rect x="20" y="36" width="10" height="30"/><rect x="36" y="26" width="10" height="40"/><rect x="52" y="14" width="10" height="52"/>
    <path d="M4 34 L28 16 L40 22 L64 4"/><path d="M54 4 H64 V14"/>
  </svg>
  <h3>EHS Consulting</h3>
  <p>MORVANT Was Established To Provide Clients In All Industries With Safety, Health, Environmental, And Security Resources That Have The Experience Necessary To Meet Unique Client</p>
  <span class="more">Read More »</span>
</div>
<div class="card active" style="left:457px;top:1383px">
  <svg width="72" height="68" viewBox="0 0 72 68" fill="none" stroke="#00a3e8" stroke-width="3">
    <path d="M8 2 H40 L50 12 V60 H8 Z"/><path d="M14 44 H22 L26 34 L30 50 L34 40 H40"/>
    <circle cx="50" cy="48" r="10"/><path d="M57 55 L66 64"/>
  </svg>
  <h3>Industrial Hygiene</h3>
  <p>MORVANT's Experienced Industrial Hygiene Network Includes Certified Industrial Hygienists Industrial Hygiene Technicians Environmental Scientists And Engineers With A Diverse Range Of</p>
  <span class="more">Read More »</span>
</div>
<div class="card" style="left:763px;top:1383px">
  <svg width="72" height="68" viewBox="0 0 72 68" fill="none" stroke="#00a3e8" stroke-width="3">
    <circle cx="46" cy="18" r="14"/><circle cx="46" cy="14" r="5"/><path d="M38 26 Q46 18 54 26"/>
    <circle cx="14" cy="30" r="6"/><path d="M4 48 Q14 36 24 48"/>
    <circle cx="14" cy="56" r="5" /><path d="M4 68 Q14 58 24 68"/>
    <circle cx="36" cy="52" r="5"/><path d="M26 66 Q36 56 46 66"/><path d="M56 30 L64 44"/>
  </svg>
  <h3>Training</h3>
  <p>MORVANT's Commitment To Industry Specific Continuing Education Has Resulted In Unparalleled Quality And Environmental Safety And Health Our Ehs Instructors Offer Custom Client Specific</p>
  <span class="more">Read More »</span>
</div>
<div class="card" style="left:150px;top:1703px">
  <svg width="72" height="68" viewBox="0 0 72 68" fill="none" stroke="#00a3e8" stroke-width="3">
    <path d="M44 4 H54 V14 H64 V24 H54 V34 H44 V24 H34 V14 H44 Z"/>
    <circle cx="26" cy="36" r="9"/><path d="M15 32 H37"/><path d="M6 66 V56 Q26 40 46 56 V66"/><path d="M20 50 V66 M32 50 V66"/>
  </svg>
  <h3>Occupational Health</h3>
  <p>MORVANT's Occupational Health Services Are Designed To Assist Businesses In Ensuring The Health Well-Being And Productivity Of Employees Our Experienced Professional Network</p>
  <span class="more">Read More »</span>
</div>
<div class="card" style="left:457px;top:1703px">
  <svg width="72" height="68" viewBox="0 0 72 68" fill="none" stroke="#00a3e8" stroke-width="3">
    <path d="M36 14 a16 16 0 0 1 10 28 V52 H26 V42 A16 16 0 0 1 36 14 Z"/><path d="M28 58 H44 M30 64 H42"/>
    <path d="M36 46 V26 Q44 28 40 36 Q36 40 36 46"/>
    <path d="M36 2 V8 M12 12 L17 17 M60 12 L55 17 M4 32 H10 M62 32 H68"/>
  </svg>
  <h3>Energy And Environment</h3>
  <p>Environmental Compliance Is No Longer Optional However There Are Smart Ways To Implement Specific Environmental Compliance Programs Reduce Energy Costs And Negotiate Permits</p>
  <span class="more">Read More »</span>
</div>
<div class="card" style="left:763px;top:1703px">
  <svg width="72" height="68" viewBox="0 0 72 68" fill="none" stroke="#00a3e8" stroke-width="3">
    <rect x="6" y="4" width="22" height="14"/><path d="M12 11 H22"/>
    <circle cx="50" cy="16" r="8"/><path d="M36 44 Q50 24 64 44"/>
    <circle cx="22" cy="34" r="8"/><path d="M8 60 Q22 40 36 60"/>
    <path d="M4 64 H68"/><path d="M40 50 H66 V64"/>
  </svg>
  <h3>Management Systems</h3>
  <p>MORVANT's Expertise In Environmental Health And Safety Management Systems Is Unmatched In The Industry Whether You Are An Organization Just Starting Management Systems</p>
  <span class="more">Read More »</span>
</div>

<div class="btn" style="left:526px;top:2031px">Contact Us</div>

<!-- COMMITMENT BAND -->
<svg class="commit-photo" width="1200" height="660" viewBox="0 2030 1200 660">
  <defs>
    <linearGradient id="netTone" x1="0" y1="0" x2="1" y2="0">
      <stop offset="0" stop-color="#0a0a0c"/><stop offset=".45" stop-color="#1a1716"/><stop offset=".7" stop-color="#5a3a22"/><stop offset="1" stop-color="#3a4a66"/>
    </linearGradient>
  </defs>
  <polygon points="0,2035 600,2181 1200,2035 1200,2520 600,2668 0,2520" fill="url(#netTone)" role="img" aria-label="Photo of a businessperson holding a tablet with glowing network connections between people icons"/>
  <polygon points="0,2033 600,2177 1200,2033 1200,2042 600,2189 0,2042" fill="#00a3e8"/>
  <polygon points="0,2514 600,2668 1200,2514 1200,2524 600,2680 0,2524" fill="#00a3e8"/>
</svg>
<h2 class="commit-title">We Are Committed To<br>Delivering Top Quality<br>Security To Our Clients.</h2>
<div class="btn" style="left:150px;top:2420px">Contact Us</div>

<!-- TESTIMONIALS -->
<h2 class="section-title" style="top:2755px">WHAT OUR CLIENTS ARE SAYING</h2>
<div class="person-card"></div>
<div class="person" style="top:2842px"><span class="avatar" role="img" aria-label="Client portrait"></span>Daniel Hollis</div>
<div class="person" style="top:2932px"><span class="avatar" role="img" aria-label="Client portrait"></span>Daniel Hollis</div>
<div class="person" style="top:3029px"><span class="avatar" role="img" aria-label="Client portrait"></span>Daniel Hollis</div>
<div class="divider"><i></i></div>

<div class="stars">★★★★★</div>
<div class="quote-title">Duis Aute Irure Dolor In Reprehenderit In Voluptate Velit Esse Cillum</div>
<p class="quote-body">Lorem Ipsum Dolor Sit Amet, Consectetur Adipiscing Elit, Sed Do Eiusmod Tempor Incididunt Ut Labore Et Dolore Magna Aliqua. Ut Enim Ad Minim Veniam, Quis Nostrud Exercitation Ullamco Laboris Nisi Ut Aliquip Ex Ea Commodo Consequat. Duis Aute Irure Dolor In Reprehenderit In Voluptate Velit Esse Cillum Dolore Eu Fugiat Nulla Pariatur. Excepteur Sint Occaecat Cupidatat Non Proident, Sunt In Culpa Qui Officia Deserunt Mollit Anim Id Est Laborum.</p>
<div class="person" style="left:554px;top:3050px;gap:20px"><span class="avatar" role="img" aria-label="Client portrait"></span>Daniel Hollis</div>

<!-- FOOTER -->
<svg class="footer-bg" width="1200" height="478" viewBox="0 3100 1200 478">
  <polygon points="0,3104 600,3250 1200,3104 1200,3578 0,3578" fill="#0d0d0d"/>
  <polygon points="0,3104 600,3238 1200,3104 1200,3112 600,3252 0,3112" fill="#00a3e8"/>
</svg>

<div class="foot-brand">MORVANT</div>
<div class="foot-sub">EHS&amp;S RESOURCES</div>
<span class="foot-social" style="left:158px;top:3433px"></span>
<span class="foot-social on" style="left:192px;top:3433px"></span>
<span class="foot-social" style="left:226px;top:3433px"></span>
<span class="foot-social" style="left:259px;top:3433px"></span>

<div class="foot-col" style="left:413px">
  <h4>Quick Links</h4>
  <ul><li>Home</li><li>About Us</li><li>Services</li><li>Security</li><li>Contact Us</li></ul>
</div>
<div class="foot-col" style="left:625px">
  <h4>Our Services</h4>
  <ul><li>EHS Consulting</li><li>Industrial Hygien</li><li>Training</li><li>Occupational Health</li><li>Energy And Environment</li><li>Management Systems</li></ul>
</div>
<div class="foot-col" style="left:867px">
  <h4>Get In Touch</h4>
  <div class="contact-item">
    <svg width="15" height="15" viewBox="0 0 24 24"><path fill="#e1251b" d="M12 2a7 7 0 0 0-7 7c0 5 7 13 7 13s7-8 7-13a7 7 0 0 0-7-7zm0 9.5A2.5 2.5 0 1 1 12 6.5a2.5 2.5 0 0 1 0 5z"/></svg>
    <div><b>Address</b>123 Lorem Ipsum Dolor Sit Amet,<br>Consectetur Adipiscing Elit</div>
  </div>
  <div class="contact-item">
    <svg width="15" height="15" viewBox="0 0 24 24"><path fill="#e1251b" d="M6.6 10.8a15 15 0 0 0 6.6 6.6l2.2-2.2c.3-.3.7-.4 1-.2 1.1.4 2.3.6 3.6.6.6 0 1 .4 1 1V20c0 .6-.4 1-1 1A17 17 0 0 1 3 4c0-.6.4-1 1-1h3.5c.6 0 1 .4 1 1 0 1.2.2 2.4.6 3.6.1.3 0 .7-.2 1z"/></svg>
    <div><b>Phone</b>555.014.2290</div>
  </div>
  <div class="contact-item">
    <svg width="15" height="15" viewBox="0 0 24 24"><path fill="#e1251b" d="M2 5h20v14H2z"/><path fill="none" stroke="#0d0d0d" stroke-width="1.6" d="M2 5l10 8 10-8"/></svg>
    <div><b>Email</b>info@morvant-example.com</div>
  </div>
</div>

<div class="foot-rule"></div>
<div class="copyright">Copyright © 2024 Morvant. All Rights Reserved.</div>

</body>
</html>
```